Velora Shift Bundle Social Media Graphics

Focusing on the Velora Shift Bundle product, create 5-6 individual social media graphics (square size). For the color scheme of the graphics, they should all be complementary with the Velora Shift Bundle bottle colors.

Note: each graphic should have one of the pictures of the bottles (2-product bundle) on it and/or one of the images with a person on it (several pics attached)/only use stock photography that I provided.

Target Market(s)

women over 40 struggling with hormonal decline

Industry/Entity Type

health and weight loss

Requirements
Nice to have
• pictures attached

```html
<!DOCTYPE html>
<html lang="en">
<head>
<meta charset="utf-8">
<title>Velora Shift Bundle – Social Media Graphics</title>
<link href="https://fonts.googleapis.com/css2?family=Archivo:wght@500;600;700;800&display=swap" rel="stylesheet">
<style>
:root{
  --teal:#5a9a98;
  --mint:#9fd2c6;
  --ink:#2b2b2b;
  --charcoal:#3d3d3d;
  --soft:#ececec;
  --paper:#ffffff;
  --stage:#d3d4d6;
  --photo-a:#e9e9e9;
  --photo-b:#c9c9c9;
}
*{margin:0;padding:0;box-sizing:border-box}
html,body{width:1200px;height:677px;overflow:hidden;background:var(--stage)}
body{font-family:'Archivo',Arial,sans-serif;color:var(--ink);text-transform:uppercase}
.grid{position:absolute;left:90px;top:18px;display:grid;grid-template-columns:repeat(3,300px);grid-template-rows:repeat(2,300px);column-gap:60px;row-gap:41px}
.post{position:relative;width:300px;height:300px;background:var(--paper);overflow:hidden;box-shadow:0 3px 8px rgba(0,0,0,.18)}
.post svg.deco{position:absolute;inset:0;width:300px;height:300px}
.photo{position:absolute;background:radial-gradient(circle at 45% 40%,var(--photo-a),var(--photo-b))}
.photo.round{border-radius:50%}
.brand{position:absolute;display:flex;align-items:center;gap:3px;font-weight:700;font-size:8px;color:var(--teal);text-transform:none;letter-spacing:.1px}
.brand i{width:9px;height:9px;border-radius:50%;background:var(--teal);display:block}
.txt{position:absolute;line-height:1.05}
.h{font-weight:800}
.s{font-weight:600}
.teal{color:var(--teal)}
.mint{color:var(--mint)}
.right{text-align:right}
.center{text-align:center}
.social{position:absolute;display:flex;gap:3px}
.social b{width:7px;height:7px;border-radius:50%;border:1px solid #555;display:block}
.pill{display:inline-block;background:var(--teal);color:#fff;border-radius:12px 0 0 12px;padding:2px 6px 1px 10px}
.bullets{list-style:none;font-weight:700;font-size:5.5px;line-height:1.9}
</style>
</head>
<body>
<main class="grid">

  <!-- Diet & Exercise -->
  <section class="post">
    <svg class="deco" viewBox="0 0 300 300">
      <circle cx="55" cy="25" r="145" fill="none" stroke="var(--mint)" stroke-width="5"/>
      <path d="M275 0 a30 30 0 0 0 25 45 v-18 a14 14 0 0 1 -10 -27z" fill="var(--teal)"/>
      <circle cx="130" cy="195" r="10" fill="var(--mint)"/>
      <circle cx="45" cy="300" r="65" fill="var(--teal)"/>
      <circle cx="115" cy="300" r="50" fill="var(--mint)"/>
      <rect x="0" y="290" width="65" height="10" fill="var(--charcoal)"/>
    </svg>
    <div class="photo round" style="left:-75px;top:-100px;width:260px;height:260px" role="img" aria-label="Product photo: the two Velora Shift Bundle bottles on a grey backdrop"></div>
    <div class="brand" style="right:16px;top:78px"><i></i>Vital Arc</div>
    <div class="txt right" style="right:18px;top:112px">
      <div class="h" style="font-size:24px">Diet &amp;</div>
      <div class="h teal" style="font-size:24px">Exercise</div>
      <div class="s" style="font-size:9.5px;line-height:1.5;margin-top:4px">Are a waste of time<br>if your hormones are<br>out of balance</div>
    </div>
    <div class="social" style="right:18px;bottom:16px"><b></b><b></b><b></b><b></b><b></b></div>
  </section>

  <!-- Weight loss / 10 years younger -->
  <section class="post">
    <svg class="deco" viewBox="0 0 300 300">
      <path d="M0 0 h45 a45 45 0 0 1 -45 45z" fill="var(--teal)"/>
      <rect x="0" y="82" width="4" height="52" fill="var(--charcoal)"/>
      <rect x="292" y="68" width="8" height="110" fill="var(--charcoal)"/>
      <path d="M100 300 a110 110 0 0 1 200 -110 v110z" fill="var(--mint)"/>
      <rect x="0" y="291" width="62" height="9" fill="var(--charcoal)"/>
    </svg>
    <div class="photo" style="left:180px;top:68px;width:112px;height:232px;border-radius:56px 56px 0 0" role="img" aria-label="Photo of a smiling woman holding both bundle bottles"></div>
    <div class="brand" style="left:118px;top:20px"><i></i>Vital Arc</div>
    <div class="txt" style="left:36px;top:58px">
      <div class="s" style="font-size:9.5px;line-height:1.4">Balance your<br>hormones to <span class="teal">accelerate</span></div>
      <div class="h mint" style="font-size:19px;margin-top:6px">Weight loss</div>
      <div class="h" style="font-size:19px">and look</div>
      <div style="display:flex;align-items:center;gap:4px;margin-top:6px">
        <span class="h mint" style="font-size:40px;line-height:.9">10</span>
        <span><span class="h teal" style="font-size:16px;display:block">Years</span><span class="h" style="font-size:11px">Younger!</span></span>
      </div>
    </div>
    <div class="social" style="left:200px;bottom:14px"><b></b><b></b><b></b><b></b><b></b></div>
  </section>

  <!-- Over 40 stubborn weight -->
  <section class="post">
    <svg class="deco" viewBox="0 0 300 300">
      <rect x="0" y="0" width="10" height="78" fill="var(--charcoal)"/>
      <circle cx="285" cy="145" r="110" fill="none" stroke="var(--mint)" stroke-width="4"/>
      <circle cx="45" cy="250" r="17" fill="var(--mint)"/>
      <path d="M150 300 a40 25 0 0 1 80 -25 h70 v25z" fill="var(--soft)"/>
      <rect x="288" y="268" width="12" height="32" fill="var(--teal)"/>
    </svg>
    <div class="photo round" style="left:170px;top:53px;width:186px;height:186px" role="img" aria-label="Photo of a blonde woman holding the bundle bottles"></div>
    <div class="brand" style="left:26px;top:64px"><i></i>Vital Arc</div>
    <div class="txt" style="left:22px;top:105px">
      <div class="h teal" style="font-size:19px">Over 40</div>
      <div class="s" style="font-size:10px;margin-top:2px">And struggling with</div>
      <div class="h mint" style="font-size:19px;margin-top:4px">Stubborn</div>
      <div class="h" style="font-size:13px;margin-top:2px">Weight gain?</div>
      <div class="s" style="font-size:8px;margin-top:8px;line-height:1.35">Try the Velora Shift<br>Bundle</div>
    </div>
    <div class="social" style="left:60px;bottom:16px"><b></b><b></b><b></b><b></b><b></b></div>
  </section>

  <!-- Balance your hormones -->
  <section class="post">
    <svg class="deco" viewBox="0 0 300 300">
      <rect x="0" y="98" width="9" height="68" fill="var(--charcoal)"/>
      <path d="M10 108 h38 a18 18 0 0 1 0 36 h-38z" fill="var(--soft)"/>
      <circle cx="78" cy="193" r="13" fill="var(--mint)"/>
      <circle cx="235" cy="160" r="110" fill="none" stroke="var(--mint)" stroke-width="4"/>
      <path d="M0 245 a55 55 0 0 1 62 55 h-20 a36 36 0 0 0 -42 -36z" fill="var(--teal)"/>
    </svg>
    <div class="photo round" style="left:138px;top:63px;width:195px;height:195px" role="img" aria-label="Photo of a smiling curly-haired woman gesturing with open hands"></div>
    <div class="brand" style="right:14px;top:20px"><i></i>Vital Arc</div>
    <div class="txt" style="left:17px;top:18px">
      <div class="s" style="font-size:9.5px">Balance your</div>
      <div class="h teal" style="font-size:24px;margin-top:3px">Hormones</div>
      <div class="h" style="font-size:12.5px;margin-top:2px">And feel like</div>
      <div class="h mint" style="font-size:12.5px;margin-top:3px">Yourself again!</div>
    </div>
    <ul class="bullets" style="position:absolute;left:20px;top:224px">
      <li>• Hot flashes &amp; night sweats</li>
      <li>• Brain fog &amp; memory lapses</li>
    </ul>
    <div class="social" style="left:68px;bottom:14px"><b></b><b></b><b></b><b></b><b></b></div>
  </section>

  <!-- Over 40 gaining weight fast -->
  <section class="post">
    <svg class="deco" viewBox="0 0 300 300">
      <rect x="94" y="0" width="110" height="10" fill="var(--charcoal)"/>
      <path d="M0 80 a40 40 0 0 1 0 80z" fill="var(--teal)"/>
      <circle cx="262" cy="104" r="12" fill="var(--mint)"/>
      <path d="M22 300 a128 128 0 0 1 256 0" fill="none" stroke="var(--mint)" stroke-width="5"/>
    </svg>
    <div class="photo" style="left:42px;top:180px;width:216px;height:120px;border-radius:108px 108px 0 0" role="img" aria-label="Photo of a joyful woman raising both fists"></div>
    <div class="brand" style="right:10px;top:14px"><i></i>Vital Arc</div>
    <div class="txt center" style="left:0;right:0;top:24px">
      <div class="h" style="font-size:16px">Over 40 and</div>
      <div class="h mint" style="font-size:17px;margin-top:3px">Gaining</div>
      <div class="h" style="font-size:20px;margin-top:3px">Weight fast?</div>
      <div class="h teal" style="font-size:8px;margin-top:5px">The solution is here!</div>
    </div>
    <div class="social" style="left:124px;top:108px"><b></b><b></b><b></b><b></b><b></b></div>
  </section>

  <!-- Hormonal symptoms -->
  <section class="post">
    <svg class="deco" viewBox="0 0 300 300">
      <path d="M140 0 h148 v22 h-148 a11 11 0 0 1 0 -22z" fill="var(--soft)"/>
      <rect x="288" y="0" width="12" height="58" fill="var(--teal)"/>
      <circle cx="58" cy="150" r="100" fill="none" stroke="var(--mint)" stroke-width="4"/>
      <circle cx="174" cy="214" r="12" fill="var(--mint)"/>
      <path d="M110 300 a30 30 0 0 1 60 0z" fill="var(--soft)"/>
      <path d="M245 300 a55 55 0 0 1 55 -55 v20 a36 36 0 0 0 -36 35z" fill="var(--teal)"/>
      <rect x="0" y="286" width="80" height="14" fill="var(--charcoal)"/>
    </svg>
    <div class="photo round" style="left:-30px;top:65px;width:170px;height:170px" role="img" aria-label="Photo of a smiling woman holding the bundle bottles beside her cheek"></div>
    <div class="brand" style="left:18px;top:16px"><i></i>Vital Arc</div>
    <div class="txt right" style="right:11px;top:80px">
      <div class="s" style="font-size:9.5px">Struggling with</div>
      <div class="h mint" style="font-size:19px;margin-top:2px">Hormonal</div>
      <div class="h" style="font-size:11px;margin-top:2px">Or perimenopause</div>
      <div class="h" style="font-size:17px;margin-top:4px;margin-right:-11px"><span class="pill">Symptoms?</span></div>
      <div class="h" style="font-size:8.5px;margin-top:6px">The solution is here!</div>
      <div class="h" style="font-size:4.6px;line-height:1.9;margin-top:3px">Mood swings •<br>Fatigue and low motivation •<br>Weight gain; stubborn belly fat •</div>
    </div>
    <div class="social" style="right:14px;top:212px"><b></b><b></b><b></b><b></b><b></b></div>
  </section>

</main>
</body>
</html>
```